Italian restaurant needs new site

Need to make our website better.

Must have reservation module

Must be able to sell wine tasting tours and wine pairing tours and intégrate with lumo desk

Blog

Social media

Wandermeter ranking and last review.

Number of Pages Required

1 page

Font styles to use
Serif

Requirements
Must have
• Reservation module
• Marketplace to buy wine pairings and gift certificates
• Wandermeter review
• Chatterbay posts
• All info from old site

```html
<!DOCTYPE html>
<html lang="en">
<head>
<meta charset="utf-8">
<title>Vinara Bistro</title>
<link href="https://fonts.googleapis.com/css2?family=Playfair+Display:wght@400;700&family=PT+Serif:ital@0;1&family=Cinzel:wght@400&display=swap" rel="stylesheet">
<style>
:root{
  --bg:#0b0806;
  --photo-a:#3a2a14;
  --photo-b:#120c07;
  --gold:#d8b25a;
  --white:#ffffff;
  --text:#f1e9dc;
  --red:#c0392b;
  --ribbon:#1d1915;
  --overlay:rgba(0,0,0,0.82);
}
*{margin:0;padding:0;box-sizing:border-box}
html,body{width:1200px;height:706px;overflow:hidden;background:var(--bg)}
.canvas{position:relative;width:1200px;height:706px;overflow:hidden;font-family:"PT Serif",serif;color:var(--text)}
.hero-photo{position:absolute;inset:0;background:radial-gradient(ellipse at 20% 40%,#6b5224 0%,transparent 45%),radial-gradient(ellipse at 85% 35%,#5a3e1a 0%,transparent 45%),linear-gradient(180deg,var(--photo-a),var(--photo-b))}
.social{position:absolute;left:18px;top:27px;display:flex;gap:12px;align-items:center}
.social span{width:11px;height:11px;border-radius:50%;background:var(--text)}
.logo-ribbon{position:absolute;left:513px;top:0;width:173px;height:168px}
.logo-name{position:absolute;left:513px;top:62px;width:173px;text-align:center;font-family:"Cinzel",serif;color:#2a1d10;font-size:24px;letter-spacing:1px}
.logo-sub{position:absolute;left:513px;top:127px;width:173px;text-align:center;font-family:"Cinzel",serif;color:#2a1d10;font-size:8px;letter-spacing:1px}
.welcome{position:absolute;top:252px;width:100%;text-align:center;font-family:"Playfair Display",serif;font-size:56px;color:var(--white)}
.tagline{position:absolute;top:380px;width:100%;text-align:center;font-family:"Playfair Display",serif;font-size:19px;letter-spacing:5px;color:var(--gold)}
.col{position:absolute;top:476px;width:238px}
.col h2{font-family:"Playfair Display",serif;font-weight:400;font-size:23px;color:var(--white);display:flex;align-items:center;gap:10px;margin-bottom:14px}
.col h2 i{width:20px;height:12px;border-radius:10px 10px 0 0;background:var(--white);display:inline-block}
.post-title{font-size:13px;color:var(--gold);margin-bottom:7px}
.post-date{font-style:italic;font-size:10px;color:var(--gold);margin-bottom:6px}
.post-body,.event-body{font-size:11.5px;line-height:19px}
.more{color:var(--red)}
.widget{width:239px;height:113px;background:#fff;color:#333;padding:6px}
.badge{width:90px;height:14px;background:#7fbf7f;border-radius:7px;margin-bottom:30px}
.widget b{display:block;font-size:11px;color:#2a4a8a;text-decoration:underline}
.widget small{display:block;font-size:9px;margin:6px 0 4px}
.dots{display:flex;gap:3px}
.dots span{width:8px;height:8px;border-radius:50%;background:#00a680}
.feed{width:239px;height:113px;background:#fff;position:relative}
.feed .cover{position:absolute;left:0;top:0;width:100%;height:66px;background:linear-gradient(90deg,#5a1010,#8a2020)}
.feed .strip{position:absolute;left:10px;top:88px;width:219px;height:20px;background:linear-gradient(90deg,#3a3a3a,#777,#3a3a3a)}
.footer{position:absolute;top:671px;left:14px;right:21px;display:flex;font-size:11px;gap:18px;align-items:center}
.footer .copy{margin-left:auto}
.footer svg{vertical-align:-2px;margin-right:5px}
.overlay{position:absolute;inset:0;background:var(--overlay)}
.burger{position:absolute;left:1138px;top:12px;width:48px;height:41px;border:1px solid #444}
.close{position:absolute;left:1168px;top:12px;font-family:"PT Serif",serif;font-size:22px;color:var(--white)}
.menu{position:absolute;top:160px;width:100%;list-style:none;text-align:center}
.menu li{height:38.8px;font-family:"Playfair Display",serif;font-size:23px;letter-spacing:3px;color:var(--white);text-transform:uppercase}
</style>
</head>
<body>
<div class="canvas">
  <div class="hero-photo" role="img" aria-label="Dim photo of wine glasses on a restaurant table"></div>
  <div class="social"><span></span><span></span><span></span><span></span><span></span>
    <svg width="13" height="10" viewBox="0 0 13 10"><rect width="13" height="10" fill="#f1e9dc"/><path d="M0 0l6.5 5L13 0" stroke="#0b0806" fill="none"/></svg></div>
  <svg class="logo-ribbon" viewBox="0 0 173 168"><path d="M0 0H173V148L86.5 168L0 148Z" fill="#efe6d6"/></svg>
  <div class="logo-name">Vinara</div>
  <div class="logo-sub">Italian Cuisine &amp; Wine Bar</div>
  <h1 class="welcome">Welcome to the Vinara Bistro</h1>
  <p class="tagline">ITALIAN CUISINE &amp; WINE BAR</p>

  <section class="col" style="left:71px">
    <h2><i></i>Blog</h2>
    <p class="post-title">Lorem Ipsum is simply dummy text</p>
    <p class="post-date">13th June, 2017</p>
    <p class="post-body">Lorem Ipsum is simply dummy text of the printing and typesetting industry. Lorem Ipsum has been the <span class="more">Read more</span></p>
  </section>
  <section class="col" style="left:341px">
    <h2><i></i>Review</h2>
    <div class="widget"><div class="badge"></div><b>Vinara Bistro</b><small>Wandermeter Traveler Rating</small>
      <div class="dots"><span></span><span></span><span></span><span></span><span></span></div></div>
  </section>
  <section class="col" style="left:612px">
    <h2><i></i>Social Media</h2>
    <div class="feed" role="img" aria-label="Chatterbay page feed with cover photo and follower thumbnails"><div class="cover"></div><div class="strip"></div></div>
  </section>
  <section class="col" style="left:882px">
    <h2><i></i>Event</h2>
    <p class="event-body">Sell wine tasting tours and wine pairing tours and integrate with lumo desk</p>
    <p class="event-body more">Read more</p>
  </section>

  <footer class="footer">
    <span><svg width="10" height="10" viewBox="0 0 10 10"><path d="M1 1h3l1 2-1.5 1a6 6 0 0 0 2.5 2.5L7 5l2 1v3C4 9 1 6 1 1z" fill="#c0392b"/></svg>152 0947</span>
    <span><svg width="8" height="11" viewBox="0 0 8 11"><path d="M4 11C1 6 0 5 0 4a4 4 0 0 1 8 0c0 1-1 2-4 7z" fill="#c0392b"/></svg>Calle Olivo 12, Centro, Puerto Lirio, Mexico</span>
    <span><svg width="10" height="10" viewBox="0 0 10 10"><circle cx="5" cy="5" r="4.5" fill="#c0392b"/><path d="M5 2v3h2" stroke="#fff" fill="none"/></svg>Open daily from 5 to 12 am</span>
    <span class="copy">© 2017 vinarabistro.com. All rights reserved.</span>
  </footer>

  <div class="overlay"></div>
  <div class="burger"></div>
  <div class="close">X</div>
  <ul class="menu">
    <li>Home</li><li>Reservation</li><li>About</li><li>Menu</li><li>Team</li><li>Gallery</li><li>Events</li><li>Blog</li><li>Testimonials</li><li>Contact</li>
  </ul>
</div>
</body>
</html>
```